Landing Page for Bathroom Remodeling Webpage - Desktop and Mobile

I am looking for some help designing the "above the fold" area for my bathroom remodeling service page. Looking for something a little different than the rest. Typically remodeling companies just put a nice picture of a bathroom remodel but I would like to do something a little different / more creative. Below is a link to the current wireframe we are working on.
Current website is located at plumvantaridge.com
Again the biggest thing I am looking for is a design for the very top section but would love help on the rest of the page as well. You will see by viewing the link below the type of information we are looking to include on the page:
PLEASE DO INCLUDE WHAT THE MOBILE VERSION WOULD LOOK LIKE AS WELL.
Wireframe:
https://boards.quillmerra.com/view/3f8a1b2c-90de-4e7a-b5c1-aa62d09e1f35-418k/
There are also comments in the link above you can read as well.
We like the idea of something interactive such as this...
https://pixorvale.com/shots/5192746-Glenhart-Scooter-Store-Animation
Attached is also the logo we want to use going forward
Target Market(s)
Residential homeowners, 30 years old+ with professional careers
Number of Pages Required
1 page
Look and feel
Each slider illustrates characteristics of the customer's brand and the style your logo design should communicate.

```html
<!DOCTYPE html>
<html lang="en">
<head>
<meta charset="utf-8">
<title>Brightmere – Bathroom Remodeling Service</title>
<link rel="stylesheet" href="https://fonts.googleapis.com/css2?family=Josefin+Sans:wght@400;600;700&family=Montserrat:wght@400;500;600;700&display=swap">
<style>
:root{
  --navy:#14203f;
  --red:#c8102e;
  --soft:#f4f1f1;
  --ink:#222a3a;
  --muted:#555c6b;
  --line:#d9d9de;
  --white:#ffffff;
}
*{box-sizing:border-box;margin:0;padding:0}
html,body{width:1200px;height:4854px;overflow:hidden}
body{position:relative;background:var(--white);font-family:"Montserrat",sans-serif;color:var(--ink)}
.abs{position:absolute}
.head{font-family:"Josefin Sans",sans-serif}
.center{text-align:center}
.btn{position:absolute;background:var(--red);color:var(--white);font-family:"Josefin Sans",sans-serif;font-weight:700;display:flex;align-items:center;justify-content:center;letter-spacing:.5px}

/* header */
.site-header{position:absolute;left:0;top:0;width:1200px;height:75px;background:var(--white)}
.brand{position:absolute;left:132px;top:20px;display:flex;align-items:center;gap:10px;font-family:"Josefin Sans",sans-serif;font-weight:700;font-size:30px;color:var(--red)}
.brand-dot{width:28px;height:28px;border-radius:50%;background:var(--navy)}
.nav a{position:absolute;top:31px;font-family:"Josefin Sans",sans-serif;font-weight:700;font-size:13px;color:var(--navy);text-decoration:none;letter-spacing:.5px}
.nav a.active{color:var(--red)}
.estimate{position:absolute;left:980px;top:0;width:220px;height:62px;background:var(--navy);clip-path:polygon(18px 0,100% 0,100% 100%,0 100%);color:var(--white)}
.estimate small{position:absolute;left:68px;top:11px;font-size:11px;letter-spacing:.5px}
.estimate strong{position:absolute;left:68px;top:26px;font-size:20px;font-weight:700}

/* hero */
.hero{position:absolute;left:0;top:75px;width:1200px;height:588px;background:linear-gradient(180deg,#e9ecee 0%,#dde2e4 45%,#cfd3d2 100%)}
.play{position:absolute;left:572px;top:160px;width:58px;height:58px;border-radius:50%;background:var(--red);box-shadow:0 0 0 6px rgba(200,16,46,.25)}
.hero h1{position:absolute;left:0;width:1200px;top:248px;text-align:center;font-family:"Josefin Sans",sans-serif;font-weight:700;font-size:36px;line-height:43px;color:var(--navy);letter-spacing:1px}

.band{position:absolute;left:0;width:1200px;background:var(--navy);color:var(--white)}
.band p{position:absolute;left:132px;font-family:"Josefin Sans",sans-serif;font-weight:600;font-size:19px;letter-spacing:.8px;line-height:26px}

.sec-title{position:absolute;left:0;width:1200px;text-align:center;font-family:"Josefin Sans",sans-serif;font-weight:600;font-size:27px;color:var(--navy)}

.project{position:absolute;top:893px;width:459px;height:320px}
.project h3{position:absolute;left:24px;top:256px;font-family:"Josefin Sans",sans-serif;font-weight:700;font-size:17px;color:var(--white);letter-spacing:.6px}
.project span{position:absolute;left:26px;top:282px;font-size:12px;color:var(--white)}
.more{position:absolute;width:120px;text-align:center;font-size:11px;color:var(--muted)}
.more i{display:block;margin:0 auto 8px;width:26px;height:26px;border:1px solid #bbb;border-radius:50%;position:relative}
.more i::before,.more i::after{content:"";position:absolute;left:12px;top:6px;width:1px;height:12px;background:#999}
.more i::after{left:6px;top:12px;width:12px;height:1px}

.split{position:absolute;left:0;top:1341px;width:1200px;height:522px;background:var(--soft)}
.split-img{position:absolute;left:0;top:0;width:629px;height:522px;background:linear-gradient(135deg,#c7cccf 0%,#eef0f0 50%,#b9bcb8 100%)}
.split h2{position:absolute;left:680px;top:48px;font-family:"Josefin Sans",sans-serif;font-weight:600;font-size:28px;line-height:38px;color:var(--navy)}
.split p{position:absolute;left:682px;top:148px;width:362px;font-size:13.5px;line-height:21.7px;color:var(--ink)}

.mat-sub{position:absolute;left:0;width:1200px;top:1962px;text-align:center;font-size:13.5px;line-height:20px;color:var(--ink)}
.mat-card{position:absolute;top:2048px;width:218px;height:288px;background:var(--white);box-shadow:0 2px 10px rgba(0,0,0,.12)}
.mat-card svg{position:absolute;left:74px;top:30px}
.mat-card h4{position:absolute;left:34px;top:130px;font-family:"Josefin Sans",sans-serif;font-weight:700;font-size:14px;color:var(--navy);letter-spacing:.5px}
.mat-card ul{position:absolute;left:34px;top:168px;list-style:none}
.mat-card li{font-size:11px;height:29px;color:var(--ink);display:flex;gap:9px}
.mat-card li::before{content:"";width:9px;height:5px;border-left:2px solid var(--navy);border-bottom:2px solid var(--navy);transform:rotate(-45deg);margin-top:2px}

.tabs{position:absolute;left:134px;top:2813px;width:934px;height:54px;border:1px solid var(--line);display:flex}
.tabs div{display:flex;align-items:center;justify-content:center;font-family:"Josefin Sans",sans-serif;font-weight:600;font-size:13px;color:var(--navy);border-right:1px solid var(--line)}
.tabs div.on{background:var(--red);color:var(--white)}
.step{position:absolute;top:2928px;width:250px;text-align:center}
.step .ring{width:98px;height:98px;border:2px solid var(--navy);border-radius:50%;margin:0 auto;display:flex;align-items:center;justify-content:center}
.step h4{margin-top:35px;font-family:"Josefin Sans",sans-serif;font-weight:700;font-size:13.5px;line-height:22px;color:var(--navy);letter-spacing:.4px}
.step p{margin-top:10px;font-size:13px;line-height:20px;color:var(--ink)}
.divider{position:absolute;top:2930px;width:1px;height:310px;background:var(--line)}

.articles{position:absolute;left:0;top:3316px;width:1200px;height:571px;background:var(--soft)}
.art{position:absolute;top:103px;width:292px;height:349px;background:var(--white)}
.art .ph{height:211px}
.art small{position:absolute;left:24px;top:242px;font-size:10px;color:var(--muted)}
.art h4{position:absolute;left:24px;top:265px;width:250px;font-family:"Josefin Sans",sans-serif;font-weight:700;font-size:13px;line-height:21px;color:var(--navy);letter-spacing:.3px}

.faq{position:absolute;left:275px;top:4007px;width:650px;height:260px;border:1px solid #888}
.faq div{position:absolute;left:34px;width:580px;height:40px;border-bottom:2px solid var(--navy);font-size:14.5px;color:var(--ink);padding-top:6px}
.faq div::after{content:"";position:absolute;right:6px;top:14px;border:5px solid transparent;border-top:6px solid var(--navy)}

.contact-box{position:absolute;top:4437px;width:309px;height:79px;border:1px solid #3a4668;color:var(--white);font-size:15px;line-height:21px}
.contact-box svg{position:absolute;left:46px;top:21px}
.contact-box p{position:absolute;left:106px;top:18px}

.footer{position:absolute;left:0;top:4557px;width:1200px;height:297px;background:var(--soft)}
.footer .fbrand{position:absolute;left:132px;top:68px;display:flex;align-items:center;gap:14px;font-family:"Josefin Sans",sans-serif;font-weight:700;font-size:42px;color:var(--red)}
.fcol{position:absolute;top:50px}
.fcol h5{font-family:"Josefin Sans",sans-serif;font-weight:700;font-size:16px;color:var(--navy);letter-spacing:.5px;margin-bottom:14px}
.fcol li{list-style:none;font-size:12px;line-height:22.4px;color:var(--ink)}
.social{position:absolute;top:141px;display:flex;gap:8px;left:402px}
.social i{width:26px;height:26px;border-radius:50%}
</style>
</head>
<body>

<header class="site-header">
  <div class="brand"><span class="brand-dot"></span>BRIGHTMERE</div>
  <nav class="nav">
    <a class="active" style="left:453px">HOME</a>
    <a style="left:523px">SERVICES</a>
    <a style="left:630px">GALLERY</a>
    <a style="left:728px">BLOG</a>
    <a style="left:803px">ABOUT</a>
    <a style="left:885px">CONTACT</a>
  </nav>
  <div class="estimate">
    <svg class="abs" style="left:30px;top:17px" width="28" height="28" viewBox="0 0 24 24" fill="none" stroke="#fff" stroke-width="1.6"><path d="M5 3h4l2 5-2.5 1.5a11 11 0 0 0 6 6L16 13l5 2v4a2 2 0 0 1-2 2A17 17 0 0 1 3 5a2 2 0 0 1 2-2z"/></svg>
    <small>GET AN ESTIMATE</small>
    <strong>555.204.3318</strong>
  </div>
</header>

<section class="hero" role="img" aria-label="Bright white bathroom with freestanding tub beneath an arched window">
  <div class="play"><svg width="58" height="58" viewBox="0 0 58 58"><path d="M23 18l17 11-17 11z" fill="#fff"/></svg></div>
  <h1>BATHROOM<br>REMODELING SERVICE</h1>
</section>

<section class="band" style="top:663px;height:111px">
  <p style="top:34px">SCHEDULE A FRESH IN HOME CONSULTATION VIA<br>OUR ONLINE APPOINTMENT SCHEDULING SYSTEM</p>
  <div class="btn" style="left:917px;top:30px;width:151px;height:46px;font-size:18px">SCHEDULE</div>
</section>

<h2 class="sec-title" style="top:822px">Get inspired by similar projects</h2>
<article class="project" style="left:132px;background:linear-gradient(160deg,#d9d6cf 0%,#a8a49a 55%,#4b4a46 100%)" role="img" aria-label="White kitchen with island and pendant lights">
  <h3>COMPLETE KITCHEN REMODEL</h3><span>in West Hollywood, CA</span>
</article>
<article class="project" style="left:610px;background:linear-gradient(160deg,#cbbfa8 0%,#8f7f66 55%,#3a332a 100%)" role="img" aria-label="Kitchen with patterned backsplash and gold chandeliers">
  <h3>KITCHEN AND COMPLETE HOME REMODEL</h3><span>in Woodland Hills, CA</span>
</article>
<div class="more" style="left:540px;top:1242px"><i></i>Show me more</div>

<section class="split">
  <div class="split-img" role="img" aria-label="White freestanding tub in a tiled bathroom with arched window"></div>
  <h2>Bathroom Remodeling<br>Made Simple</h2>
  <p>Bathroom remodel can be complex, but when completed in an eco-friendly and sustainable manner can also drastically decrease monthly bills and give you the satisfaction of reducing your carbon footprint in the process. A bathroom remodels ranges anywhere from updating your plumbing fixture, to making more efficient use of the space, to building the in-home spa of your dreams. A bathroom remodel is subjective, but homeowners are generally faced with the same universal challenges regardless of project scope.</p>
  <div class="more" style="left:671px;top:423px"><i></i>Show me more</div>
</section>

<h2 class="sec-title" style="top:1910px">Material Selections</h2>
<p class="mat-sub">For your bathroom remodel there will be material selections you will have to make.<br>Use the lists below to get an idea of some of the options.</p>

<div class="mat-card" style="left:132px">
  <svg width="70" height="70" viewBox="0 0 70 70" fill="none" stroke="#14203f" stroke-width="4"><circle cx="35" cy="35" r="27"/><path d="M40 14L24 38h12l-6 18 16-24H34z" fill="#14203f" stroke-width="2"/></svg>
  <h4>ELECTRICAL</h4><ul><li>Light Fixtures</li><li>Heated Floor</li><li>Outlets</li></ul>
</div>
<div class="mat-card" style="left:371px">
  <svg width="70" height="70" viewBox="0 0 70 70" fill="none" stroke="#14203f" stroke-width="4"><path d="M50 8v22H30v20H16"/><path d="M44 8h12M44 22h12M24 44v12M10 62h14"/><path d="M16 52v14"/></svg>
  <h4>PLUMBING</h4><ul><li>Vanity Fixtures</li><li>Shower Fixtures</li><li>Toilet</li></ul>
</div>
<div class="mat-card" style="left:612px">
  <svg width="70" height="70" viewBox="0 0 70 70" fill="none" stroke="#14203f" stroke-width="4"><rect x="10" y="8" width="14" height="54" rx="6"/><path d="M24 18h36v44H17"/><path d="M32 30h22M32 40h22M32 50h22M43 30v30"/><circle cx="17" cy="54" r="3"/></svg>
  <h4>TILE &amp; FLOORING</h4><ul><li>Shower Wall Tile</li><li>Shower Floor Tile</li><li>Bathroom Flooring</li></ul>
</div>
<div class="mat-card" style="left:852px">
  <svg width="70" height="70" viewBox="0 0 70 70" fill="#14203f"><rect x="12" y="6" width="44" height="14"/><path d="M56 12h6v18H36v8h-5V25h26z"/><rect x="29" y="38" width="9" height="28"/></svg>
  <h4>FINISHES</h4><ul><li>Trim</li><li>Mirrors &amp; Tower Bars</li><li>Cabinetry &amp; Counter Tops</li></ul>
</div>

<section class="abs" style="left:0;top:2389px;width:1200px;height:247px;background:var(--soft)">
  <h2 class="sec-title" style="top:48px">Pricing Packages</h2>
  <p class="abs center" style="left:0;width:1200px;top:97px;font-size:20px;color:var(--ink)">Pricing for basement finishes can vary dramatically</p>
  <div class="btn" style="left:522px;top:152px;width:164px;height:48px;font-size:19px">BOOK NOW</div>
</section>

<section class="band" style="top:2636px;height:120px">
  <p style="top:50px">SCHEDULE YOUR FREE CONSULTATION TODAY!</p>
  <div class="btn" style="left:855px;top:39px;width:213px;height:44px;font-size:18px">SCHEDULE BELOW</div>
</section>

<div class="tabs">
  <div class="on" style="width:318px">CHOOSE APPOINTMENT</div>
  <div style="width:322px">YOUR INFO</div>
  <div style="width:294px;border-right:0">CONFIRMATION</div>
</div>

<div class="step" style="left:116px">
  <div class="ring"><svg width="54" height="54" viewBox="0 0 54 54" fill="none" stroke="#14203f" stroke-width="2.4"><rect x="6" y="10" width="36" height="32" rx="3"/><path d="M6 19h36M14 6v8M34 6v8M13 26h4M22 26h4M31 26h4M13 33h4M22 33h4"/><circle cx="40" cy="40" r="9" fill="#fff"/><path d="M36 40l3 3 5-6"/></svg></div>
  <h4>SCHEDULE AN<br>APPOINTMENT TODAY</h4>
  <p>View our calendar on the left and pick an appointment time that works best for you.</p>
</div>
<div class="divider" style="left:418px"></div>
<div class="step" style="left:474px">
  <div class="ring"><svg width="54" height="54" viewBox="0 0 54 54" fill="none" stroke="#14203f" stroke-width="2.6"><path d="M27 6l6 13 14 1.5-10.5 9.5 3 14L27 37l-12.5 7 3-14L7 20.5 21 19z" stroke-linejoin="round"/></svg></div>
  <h4>REVIEW OUR "THINGS TO<br>THINK ABOUT CHECKLIST"</h4>
  <p>There are a lot of things that go into a remodel. To prepare for our visit review the 'Things to think about Checklist' here. help you prepare for some of the questions we may ask depending on the project.</p>
</div>
<div class="divider" style="left:788px"></div>
<div class="step" style="left:834px">
  <div class="ring"><svg width="54" height="54" viewBox="0 0 54 54" fill="none" stroke="#14203f" stroke-width="2.4"><rect x="7" y="10" width="40" height="34" rx="3"/><path d="M7 19h40M15 6v8M23 6v8M31 6v8M39 6v8M14 26h4M22 26h4M30 26h4M38 26h3M14 34h4M22 34h4M30 34h4"/></svg></div>
  <h4 style="margin-top:44px">APPOINTMENT</h4>
  <p>One of our project managers will meet with you to discuss the project. At this initial stage we will be taking measurements and listening to your vision for the space.</p>
</div>

<section class="articles">
  <h2 class="sec-title" style="top:38px">Helpful Articles</h2>
  <article class="art" style="left:132px"><div class="ph" role="img" aria-label="Bathroom vanity with round mirror" style="background:linear-gradient(180deg,#e4e3df 0%,#b7a88e 60%,#2f2c29 100%)"></div><small>03/01/2021</small><h4>LOREM IPSUM IS SIMPLY DUMMY TEXT OF THE PRINTING AND TYPESETTING INDUSTRY.</h4></article>
  <article class="art" style="left:454px"><div class="ph" role="img" aria-label="White bathroom with double vanity and pendant lights" style="background:linear-gradient(180deg,#d9d6cf 0%,#efeeea 50%,#5a5c60 100%)"></div><small>03/01/2021</small><h4>LOREM IPSUM IS SIMPLY DUMMY TEXT OF THE PRINTING AND TYPESETTING INDUSTRY.</h4></article>
  <article class="art" style="left:776px"><div class="ph" role="img" aria-label="Bathtub in front of a stone feature wall" style="background:linear-gradient(180deg,#8a7a68 0%,#6c5f52 55%,#3b3430 100%)"></div><small>03/01/2021</small><h4>LOREM IPSUM IS SIMPLY DUMMY TEXT OF THE PRINTING AND TYPESETTING INDUSTRY.</h4></article>
  <div class="btn" style="left:522px;top:488px;width:156px;height:41px;font-size:14px">READ OUR BLOG</div>
</section>

<h2 class="sec-title" style="top:3937px">Frequently Asked Questions</h2>
<div class="faq">
  <div style="top:30px">How much does a basement finish cost?</div>
  <div style="top:88px">How long will it take?</div>
  <div style="top:145px">Do you pull Permits?</div>
  <div style="top:203px">Are you licensed and insured?</div>
</div>

<section class="abs" style="left:0;top:4326px;width:1200px;height:231px;background:var(--navy)">
  <h2 class="sec-title" style="top:42px;color:#fff">Other Questions?</h2>
</section>
<div class="contact-box" style="left:262px">
  <svg width="36" height="36" viewBox="0 0 24 24" fill="none" stroke="#fff" stroke-width="1.4"><path d="M5 3h4l2 5-2.5 1.5a11 11 0 0 0 6 6L16 13l5 2v4a2 2 0 0 1-2 2A17 17 0 0 1 3 5a2 2 0 0 1 2-2z"/><path d="M14 3a7 7 0 0 1 7 7M14 7a3 3 0 0 1 3 3"/></svg>
  <p>Contact Us<br>555.204.3318</p>
</div>
<p class="abs" style="left:587px;top:4467px;color:#fff;font-size:15px">OR</p>
<div class="contact-box" style="left:625px">
  <svg width="44" height="38" viewBox="0 0 44 38" fill="none" stroke="#fff" stroke-width="2"><rect x="2" y="2" width="28" height="20" rx="2"/><path d="M8 9h16M8 15h12M10 22l-4 6v-6"/><path d="M30 12h10v18h-4v5l-6-5H16v-8"/><path d="M22 26h12"/></svg>
  <p>Reach out to our<br><b>Support Team</b></p>
</div>

<footer class="footer">
  <div class="fbrand"><span class="brand-dot" style="width:46px;height:46px"></span>BRIGHTMERE</div>
  <p class="abs head" style="left:327px;top:147px;font-weight:700;font-size:13px;color:var(--navy)">FOLLOW</p>
  <div class="social"><i style="background:#3b5a9a"></i><i style="background:#2d9ad9"></i><i style="background:var(--navy)"></i></div>
  <p class="abs" style="left:208px;top:194px;font-size:12px;color:var(--ink)">Copyright ©2021 Brightmere All Rights Reserved</p>
  <div class="fcol" style="left:612px"><h5>SERVICES</h5><ul><li>Basement Finishing</li><li>Bathroom Remodeling</li><li>Handyman</li><li>Kitchen Remodeling</li><li>Window Replacement</li><li>Whole Home Remodeling</li></ul></div>
  <div class="fcol" style="left:902px"><h5>SERVICE AREAS</h5><ul><li>Ankeny, IA</li><li>Clive, IA</li><li>Des Moines, IA</li><li>Johnston, IA</li><li>Urbandale, IA</li><li>Waukee, IA</li><li>West Des Moines, IA</li><li>View All</li></ul></div>
</footer>

</body>
</html>
```